Website for residential builder repair in Australia

I currently have my website setup using Hostinger as hosting and started playing around with Wordpress.
I would like this to be able to be imported into Wordpress after built so I can add blog posts and edit site if needed.

I would like a website built that is simple and clear.

the main colours id like for the site are black and white and maybe grey.

I would like a simple welcome page, an about us page, a project page, and a blog page where I can write small articles.

will need to display licence number on website lic. 374026K

Target Market(s)

young to middle age families and couples looking to build a sustainable and high performance house.

Contact Information for Business Card

Quarry Lane Building
Lic. 374026K (to be printed small)
email; miles@quarrylanebuilding.com.au
phone : 0428163950

Miles Venner - Director

Number of Pages Required

4 page

Font styles to use
Sans Serif
Other font styles liked:
• match logo

Colors

Designer to choose only greyscale colors for use in the design.

Requirements
Must have
• outline of works

Certified Passive House Tradesperson
New Builds
Renovations
Architectural homes
Nice to have
• thinking dark grey background or black

would like to see the logo embossed to look slightly 3d

back of card to be white or light grey so It can be written on.

letterhead to contain licence number swell

```html
<!DOCTYPE html>
<html lang="en">
<head>
<meta charset="utf-8">
<title>Quarry Lane Building</title>
<link rel="stylesheet" href="https://fonts.googleapis.com/css2?family=Mulish:wght@300;400;600;700;800&display=swap">
<style>
:root{
  --accent:#d6d6d6;
  --accent-dark:#7c7c7c;
  --ink:#1f1f1f;
  --ink-deep:#121212;
  --slate:#2a2a2a;
  --slate-card:#3c3c3c;
  --text-grey:#8a8a8a;
  --soft-bg:#f4f4f4;
  --action:#4a4a4a;
  --white:#ffffff;
  --line:#e3e3e3;
  --foot-text:#a9a9a9;
}
*{box-sizing:border-box;margin:0;padding:0}
html,body{width:1200px;height:3110px;overflow:hidden}
body{font-family:"Mulish",sans-serif;color:var(--ink);background:var(--white);position:relative}
.abs{position:absolute}
.btn{position:absolute;display:flex;align-items:center;justify-content:center;font-size:10px;font-weight:600;text-decoration:none}
.btn-accent{background:var(--accent);color:var(--ink)}

/* header + hero */
.hero{position:absolute;left:0;top:0;width:1200px;height:519px;background:linear-gradient(120deg,#6f6f6f 0%,#535353 45%,#616161 70%,#444 100%)}
.brand{position:absolute;left:274px;top:16px;color:var(--white);font-size:15px;font-weight:400;letter-spacing:3px;line-height:18px;white-space:nowrap}
.brand small{display:block;font-size:7px;letter-spacing:6px;margin-top:4px}
.nav{position:absolute;top:21px;left:536px}
.nav a{position:absolute;color:#eaeaea;font-size:10px;text-decoration:none;white-space:nowrap}
.nav-cta{position:absolute;left:803px;top:14px;width:124px;height:27px;border:1px solid #fff;border-radius:2px;color:#fff;font-size:8.5px;font-weight:700;display:flex;align-items:center;justify-content:center}
.hero-kicker{left:264px;top:167px;font-size:8px;font-weight:800;color:#fff}
.hero-title{left:264px;top:190px;font-size:36px;font-weight:400;color:#fff;white-space:nowrap}
.hero-text{left:264px;top:244px;width:345px;font-size:9px;line-height:16.5px;color:#efefef}
.hero-link{left:407px;top:322px;font-size:10px;color:#fff}
.hero-address{left:264px;top:444px;font-size:9px;color:#efefef;display:flex;align-items:center;gap:8px}
.socials{left:264px;top:477px;display:flex;gap:3px}
.socials span{width:20px;height:20px;border-radius:50%;background:#fff;display:block}

/* estimate form */
.estimate-card{position:absolute;left:645px;top:461px;width:291px;height:378px;background:#fff;box-shadow:0 18px 40px rgba(0,0,0,.13)}
.estimate-card h3{position:absolute;top:41px;width:100%;text-align:center;font-size:13px;font-weight:600}
.field{position:absolute;left:26px;width:238px;height:24px;background:#f7f7f7;border:1px solid var(--line);font-size:8px;color:#9c9c9c;padding:7px}
.send-btn{left:26px;top:299px;width:99px;height:26px;background:var(--action);color:#fff}
.required{position:absolute;left:196px;top:315px;font-size:7.5px;color:#9c9c9c;display:flex;align-items:center;gap:4px}
.required i{width:4px;height:4px;border-radius:50%;background:var(--accent-dark);display:block}

/* about */
.about-title{left:264px;top:565px;font-size:26px;font-weight:400}
.about-lead{left:264px;top:612px;width:305px;font-size:9px;font-weight:700;line-height:16.5px;color:var(--text-grey)}
.about-text{left:264px;top:655px;width:305px;font-size:9px;line-height:16.5px;color:var(--text-grey)}
.about-more{left:264px;top:758px;width:85px;height:25px}
.phone-dot{left:264px;top:797px;width:30px;height:30px;border-radius:50%;background:#ededed;display:flex;align-items:center;justify-content:center}
.emergency{left:309px;top:796px;font-size:7.5px;font-weight:800}
.emergency-num{left:309px;top:810px;font-size:20px;color:var(--accent-dark);font-weight:400}

/* services */
.services{position:absolute;left:0;top:929px;width:1200px;height:288px;display:flex}
.service{position:relative;width:300px;height:288px;color:#fff}
.service .num{position:absolute;left:22px;top:24px;font-size:13px;font-weight:700}
.service h4{position:absolute;left:22px;font-size:18px;font-weight:400;line-height:20px;width:240px}
.service p{position:absolute;left:22px;width:255px;font-size:8.5px;line-height:16px;color:#e6e6e6}
.service .more{position:absolute;left:22px;font-size:9px;font-weight:700}
.svc1{background:linear-gradient(160deg,#3a3a3a 0%,#4a4a4a 35%,#5c5c5c 60%,#3e3e3e 100%)}
.svc2{background:linear-gradient(160deg,#505050 0%,#6a6a6a 40%,#3c3c3c 100%)}
.svc3{background:linear-gradient(160deg,#484848 0%,#6b6b6b 45%,#4d4d4d 100%)}
.svc4{background:linear-gradient(160deg,#2f2f2f 0%,#454545 45%,#2c2c2c 100%)}

/* why choose */
.why{position:absolute;left:0;top:1217px;width:1200px;height:645px;background:var(--slate)}
.why h2{position:absolute;top:118px;width:100%;text-align:center;color:#fff;font-size:26px;font-weight:400}
.why .intro{position:absolute;left:370px;top:158px;width:460px;text-align:center;color:#e6e6e6;font-size:9px;line-height:16.5px}
.feature{position:absolute;width:206px;height:158px;background:var(--slate-card);color:#fff}
.feature svg{position:absolute;left:27px;top:28px}
.feature h5{position:absolute;left:23px;top:63px;font-size:13.5px;font-weight:600}
.feature p{position:absolute;left:23px;top:86px;width:165px;font-size:8.5px;line-height:16.5px;color:#d4d4d4}

/* testimonial */
.testimonial{position:absolute;left:0;top:1862px;width:1200px;height:429px;background:var(--soft-bg)}
.testimonial-photo{position:absolute;left:0;top:0;width:543px;height:429px;background:linear-gradient(90deg,#d0d0d0 0%,#b4b4b4 55%,#6e6e6e 72%,#f4f4f4 100%)}
.t-kicker{left:600px;top:62px;font-size:7.5px;font-weight:800}
.t-quote{left:600px;top:78px;width:330px;font-size:18.5px;line-height:21.5px;font-weight:400}
.t-name{left:600px;top:242px;font-size:9px;font-weight:600}
.t-role{left:600px;top:256px;font-size:8.5px;color:var(--text-grey)}
.review{position:absolute;top:2291px;width:224px;height:268px;background:#fff}
.review .mark{position:absolute;left:27px;top:26px;color:#a8a8a8;font-size:20px;font-weight:800}
.review p{position:absolute;left:27px;top:58px;width:176px;font-size:12px;line-height:17.6px;color:var(--text-grey)}
.review .who{position:absolute;left:27px;display:flex;align-items:center;gap:9px}
.review .who i{width:21px;height:21px;border-radius:50%;background:#707070;display:block}
.review .who b{display:block;font-size:9px;font-weight:600;color:var(--ink)}
.review .who span{display:block;font-size:7.5px;color:var(--text-grey)}

/* cta + footer */
.cta{position:absolute;left:0;top:2610px;width:1200px;height:247px;background:var(--ink-deep)}
.cta h2{position:absolute;left:264px;top:65px;color:#fff;font-size:26px;font-weight:400}
.cta p{position:absolute;left:264px;top:109px;width:310px;color:#e6e6e6;font-size:9px;line-height:16.5px}
.cta .btn-call{left:407px;top:154px;width:108px;height:26px;border:1px solid #fff;color:#fff;gap:8px}
.footer{position:absolute;left:0;top:2857px;width:1200px;height:253px;background:var(--ink-deep);color:#fff}
.footer .brand{top:62px}
.footer h6{position:absolute;top:57px;font-size:13px;font-weight:400}
.footer ul{position:absolute;top:90px;list-style:none}
.footer li{font-size:8px;line-height:17px;color:var(--foot-text);display:flex;align-items:center;gap:9px;white-space:nowrap}
.footer .link{position:absolute;font-size:9px;font-weight:700}
.footer .copy{position:absolute;top:222px;font-size:8.5px;color:var(--foot-text)}
</style>
</head>
<body>

<header class="hero" role="img" aria-label="Photo of a modern angular glass building against a grey sky">
  <div class="brand">QUARRY LANE<small>BUILDING</small></div>
  <nav class="nav">
    <a style="left:0;font-weight:700;color:#fff">Home</a>
    <a style="left:42px">About Us</a>
    <a style="left:99px">Services</a>
    <a style="left:151px">Projects</a>
    <a style="left:203px">Contact Us</a>
  </nav>
  <div class="nav-cta">Get a Free Estimate</div>

  <div class="abs hero-kicker">Best Building And Repairing</div>
  <h1 class="abs hero-title">Lorem ipsum dolor sit amet</h1>
  <p class="abs hero-text">Vestibulum, diam vulputate amet cras in diam quis turpis curabitur tellus aliquet tellus iaculis tempus, sollicitudin massa duis eleifend egestas turpis sit etiam commodo viverra lacinia.</p>
  <a class="btn btn-accent" style="left:264px;top:315px;width:124px;height:27px">Get a Free Estimate</a>
  <div class="abs hero-link">View Our Services &nbsp;→</div>
  <div class="abs hero-address">
    <svg width="7" height="9" viewBox="0 0 7 9"><path d="M3.5 0a3.5 3.5 0 0 0-3.5 3.5C0 6 3.5 9 3.5 9S7 6 7 3.5A3.5 3.5 0 0 0 3.5 0zm0 5a1.5 1.5 0 1 1 0-3 1.5 1.5 0 0 1 0 3z" fill="#fff"/></svg>
    42 Ridgeway Road, Ballarat VIC 3350
  </div>
  <div class="abs socials"><span></span><span></span><span></span></div>
</header>

<section class="estimate-card">
  <h3>Request A Free Estimate</h3>
  <div class="field" style="top:74px">Full name*</div>
  <div class="field" style="top:111px">Active email*</div>
  <div class="field" style="top:148px">Phone number*</div>
  <div class="field" style="top:185px">Subject*</div>
  <div class="field" style="top:221px;height:67px">Message*</div>
  <a class="btn send-btn">Send Request</a>
  <div class="required"><i></i>Required Fields</div>
</section>

<section class="about">
  <h2 class="abs about-title">About Us</h2>
  <p class="abs about-lead">Condimentum ultrices vitae dictumst augue id porta sed accumsan ut amet varius nibh neque faucibus iaculis interdum erat eget.</p>
  <p class="abs about-text">Rutrum ut volutpat scelerisque auctor ultrices lectus ultrices ullamcorper massa diam etiam amet a, nulla pulvinar sapien, ornare lectus nullam a faucibus diam et lorem diam nullam commodo, vestibulum, pulvinar nisl suspendisse diam venenatis enim nunc integer orci quam risus sit neque, fusce massa vulputate pretium.</p>
  <a class="btn btn-accent about-more">Read More</a>
  <div class="abs phone-dot">
    <svg width="12" height="12" viewBox="0 0 24 24"><path d="M6.6 10.8a15.1 15.1 0 0 0 6.6 6.6l2.2-2.2c.3-.3.7-.4 1-.2 1.1.4 2.3.6 3.6.6.6 0 1 .4 1 1V20c0 .6-.4 1-1 1A17 17 0 0 1 3 4c0-.6.4-1 1-1h3.5c.6 0 1 .4 1 1 0 1.3.2 2.5.6 3.6.1.3 0 .7-.2 1z" fill="#7c7c7c"/></svg>
  </div>
  <div class="abs emergency">24/7 Emergency Roofing Service.</div>
  <div class="abs emergency-num">0428 163 950</div>
</section>

<section class="services">
  <article class="service svc1" role="img" aria-label="Photo of a brick house under a clear sky">
    <span class="num">01.</span>
    <h4 style="top:154px">Certified Passive House Tradesperson</h4>
    <p style="top:201px">Ut amet, risus aliquam sapien amet porta magna quam dictum arcu magna et dolor diam ultricies.</p>
    <span class="more" style="top:252px">Learn More &nbsp;&nbsp;→</span>
  </article>
  <article class="service svc2" role="img" aria-label="Photo of new gabled townhouses">
    <span class="num">02.</span>
    <h4 style="top:154px">New Builds</h4>
    <p style="top:181px">Aliquam orci blandit non risus viverra sed iaculis nunc neque augue tincidunt diam turpis nisl.</p>
    <span class="more" style="top:232px">Learn More &nbsp;&nbsp;→</span>
  </article>
  <article class="service svc3" role="img" aria-label="Photo of roofers renovating a row of houses">
    <span class="num">03.</span>
    <h4 style="top:154px">Renovations</h4>
    <p style="top:181px">Amet proin sed ac ut diam varius pharetra tortor eget augue massa pretium turpis praesent.</p>
    <span class="more" style="top:232px">Learn More &nbsp;&nbsp;→</span>
  </article>
  <article class="service svc4" role="img" aria-label="Photo of hands holding banknotes over a desk">
    <span class="num">04.</span>
    <h4 style="top:154px">Architectural Homes</h4>
    <p style="top:179px">Sed ac, morbi vel viverra scelerisque tellus arcu eget ut duis fames in quam gravida.</p>
    <span class="more" style="top:229px">Learn More &nbsp;&nbsp;→</span>
  </article>
</section>

<section class="why">
  <h2>Why Choose Us</h2>
  <p class="intro">Ipsum ornare eu nibh sagittis nunc quisque viverra fringilla egestas dictumst nisl, vestibulum diam nisi suscipit eros, consectetur sapien nullam mi facilisis magna sem</p>

  <div class="feature" style="left:264px;top:228px">
    <svg width="14" height="14" viewBox="0 0 14 14"><path d="M3 1h8v4a4 4 0 0 1-8 0zM6 9h2v2h2v2H4v-2h2z" fill="#d6d6d6"/></svg>
    <h5>Qualified Expert</h5>
    <p>Ut amet, risus aliquam sapien amet porta magna quam dictum arcu magna et dolor diam ultricies.</p>
  </div>
  <div class="feature" style="left:497px;top:228px">
    <svg width="14" height="14" viewBox="0 0 14 14"><circle cx="7" cy="7" r="4.5" fill="#d6d6d6"/></svg>
    <h5>Workmanship Quality</h5>
    <p>Ut amet, risus aliquam sapien amet porta magna quam dictum arcu magna et dolor diam ultricies.</p>
  </div>
  <div class="feature" style="left:730px;top:228px">
    <svg width="14" height="14" viewBox="0 0 14 14"><path d="M2 11a5 5 0 0 1 10 0zM1 11h12v2H1z" fill="#d6d6d6"/></svg>
    <h5>Quality Professionals</h5>
    <p>Ut amet, risus aliquam sapien amet porta magna quam dictum arcu magna et dolor diam ultricies.</p>
  </div>
  <div class="feature" style="left:264px;top:413px">
    <svg width="14" height="14" viewBox="0 0 14 14"><circle cx="7" cy="7" r="6" fill="#d6d6d6"/><path d="M7 3.5V7l2 1.5" stroke="#3c3c3c" stroke-width="1.4" fill="none"/></svg>
    <h5>Flexible Schedule</h5>
    <p>Sem in eget faucibus massa arcu et elementum sed massa nulla dolor felis dictumst malesuada non.</p>
  </div>
  <div class="feature" style="left:497px;top:413px">
    <svg width="14" height="14" viewBox="0 0 14 14"><rect x="1" y="2" width="12" height="11" rx="1.5" fill="#d6d6d6"/><rect x="1" y="5" width="12" height="1.2" fill="#3c3c3c"/></svg>
    <h5>Affordable Package</h5>
    <p>Sem in eget faucibus massa arcu et elementum sed massa nulla dolor felis dictumst malesuada non.</p>
  </div>
  <div class="feature" style="left:730px;top:413px">
    <svg width="14" height="14" viewBox="0 0 14 14"><path d="M1 1h6l6 6-6 6-6-6z" fill="#d6d6d6"/><circle cx="4" cy="4" r="1.1" fill="#3c3c3c"/></svg>
    <h5>Special Offer</h5>
    <p>Sem in eget faucibus massa arcu et elementum sed massa nulla dolor felis dictumst malesuada non.</p>
  </div>
</section>

<section class="testimonial">
  <div class="testimonial-photo" role="img" aria-label="Photo of a client standing in front of old town houses"></div>
  <div class="abs t-kicker">Here's What Our Client Say About Us</div>
  <blockquote class="abs t-quote">“Quis Sed Sagittis Lorem Eget Venenatis, Enim Nisl Tellus Sem Convallis Diam Vitae Arcu Odio Bibendum Eu Pretium Dolor Aliquam Scelerisque Tortor, Odio Euismod.”</blockquote>
  <div class="abs t-name">Clara Hollis</div>
  <div class="abs t-role">Manager of Finance Consultant</div>
</section>

<article class="review" style="left:264px">
  <span class="mark">“</span>
  <p>Penatibus eros congue aliquet lectus in imperdiet vel mattis sed enim enim pulvinar posuere augue duis lorem lectus at facilisi in nibh at quam in justo, sit auctor morbi eget aliquam lorem gravida fringilla pretium vestibulum mauris.</p>
  <div class="who" style="top:213px"><i></i><div><b>Peter Lindgard</b><span>CEO of Manufacture Company</span></div></div>
</article>
<article class="review" style="left:488px">
  <span class="mark">“</span>
  <p>Erat elit et, amet eget morbi enim, potenti urna, blandit tincidunt faucibus eu diam tincidunt interdum pharetra et diam viverra lacinia integer quam iaculis facilisis viverra quam leo proin semper aenean morbi fames integer vitae ipsum.</p>
  <div class="who" style="top:230px"><i></i><div><b>Nadia Ferris</b><span>Graphic Designer</span></div></div>
</article>
<article class="review" style="left:712px">
  <span class="mark">“</span>
  <p>Neque amet at sit elementum et proin lacus vestibulum amet bibendum purus dolor turpis platea sodales senectus purus donec elit molestie scelerisque amet nullam tincidunt arcu odio enim ut nunc vel, tristique dictumst adipiscing elit ultrices.</p>
  <div class="who" style="top:213px"><i></i><div><b>Owen T. Marlow</b><span>Song Writer</span></div></div>
</article>

<section class="cta">
  <h2>Need A Free Estimate?</h2>
  <p>Rutrum ut volutpat scelerisque auctor ultrices lectus ultrices ullamcorper massa diam etiam amet a, nulla pulvinar sapien.</p>
  <a class="btn btn-accent" style="left:264px;top:154px;width:124px;height:26px">Get a Free Estimate</a>
  <a class="btn btn-call">
    <svg width="9" height="9" viewBox="0 0 24 24"><path d="M6.6 10.8a15.1 15.1 0 0 0 6.6 6.6l2.2-2.2c.3-.3.7-.4 1-.2 1.1.4 2.3.6 3.6.6.6 0 1 .4 1 1V20c0 .6-.4 1-1 1A17 17 0 0 1 3 4c0-.6.4-1 1-1h3.5c.6 0 1 .4 1 1 0 1.3.2 2.5.6 3.6.1.3 0 .7-.2 1z" fill="#fff"/></svg>
    Call Us Now
  </a>
</section>

<footer class="footer">
  <div class="brand">QUARRY LANE<small>BUILDING</small></div>

  <h6 style="left:432px">Contact Info</h6>
  <ul style="left:432px">
    <li><svg width="7" height="9" viewBox="0 0 7 9"><path d="M3.5 0a3.5 3.5 0 0 0-3.5 3.5C0 6 3.5 9 3.5 9S7 6 7 3.5A3.5 3.5 0 0 0 3.5 0z" fill="#fff"/></svg>42 Ridgeway Road, Ballarat VIC 3350</li>
    <li><svg width="8" height="8" viewBox="0 0 24 24"><path d="M6.6 10.8a15.1 15.1 0 0 0 6.6 6.6l2.2-2.2c.3-.3.7-.4 1-.2 1.1.4 2.3.6 3.6.6.6 0 1 .4 1 1V20c0 .6-.4 1-1 1A17 17 0 0 1 3 4c0-.6.4-1 1-1h3.5c.6 0 1 .4 1 1 0 1.3.2 2.5.6 3.6.1.3 0 .7-.2 1z" fill="#fff"/></svg>0428 163 950</li>
    <li><svg width="8" height="7" viewBox="0 0 8 7"><rect width="8" height="7" fill="#fff"/><path d="M0 0l4 3.5L8 0" stroke="#121212" fill="none"/></svg>miles@quarrylanebuilding.com.au</li>
  </ul>
  <div class="link" style="left:432px;top:157px">Get Directions &nbsp;→</div>

  <h6 style="left:600px">Quick Links</h6>
  <ul style="left:600px">
    <li>Home</li><li>About Us</li><li>Services</li><li>Projects</li><li>Contact Us</li>
  </ul>
  <ul style="left:683px">
    <li>Installation</li><li>Replacement</li><li>Repair</li><li>After Storm Damage</li><li>Finance &amp; Insurance</li>
  </ul>

  <h6 style="left:801px">Our Service</h6>
  <ul style="left:801px">
    <li>Commercial Roofing</li><li>Residential Roofing</li><li>After Storm Damage</li><li>Finance &amp; Insurance</li>
  </ul>
  <div class="link" style="left:801px;top:164px">Get a Free Estimate &nbsp;→</div>

  <div class="copy" style="left:264px">Copyright © 2020 Quarry Lane Building</div>
  <div class="copy" style="left:824px">Powered by Quarry Lane Building</div>
</footer>

</body>
</html>
```